Legal Service Estimated Retainer and Average Case Value

We need an 11x14 flyer that contains the standard retainers and average cost be case, both provided in documents, for each case type we handle. We need the information displayed, preferably in a way that makes the information readable but less troubling to a client shocked at price of litigation. We need one sheet with the retainers and average case value merged into one table.

Target Market(s)

Potential Clients

Font styles to use
Serif
Sans Serif

```html
<!DOCTYPE html>
<html lang="en">
<head>
<meta charset="utf-8">
<title>Average Fee Per Case Type</title>
<link href="https://fonts.googleapis.com/css2?family=Lato:wght@400;700&display=swap" rel="stylesheet">
<style>
  :root {
    --ink: #3b3b91;
    --band: #9bdcf6;
    --rule: #2a2a3a;
    --paper: #ffffff;
  }
  * { margin: 0; padding: 0; box-sizing: border-box; }
  html, body { width: 966px; height: 1200px; overflow: hidden; background: var(--paper); }
  body { font-family: "Lato", Arial, sans-serif; color: var(--ink); position: relative; }

  .brand {
    position: absolute; left: 36px; top: 34px;
    display: flex; align-items: center; gap: 10px;
  }
  .brand-mark { width: 40px; height: 40px; background: var(--ink); }
  .brand-name {
    font-weight: 700; color: var(--ink);
    font-size: 15px; line-height: 1.15; letter-spacing: 0.5px;
  }
  .brand-name small { display: block; font-size: 9px; letter-spacing: 1px; }

  .title {
    position: absolute; left: 0; width: 966px; top: 142px;
    text-align: center; font-weight: 700; font-size: 33px;
  }
  .intro {
    position: absolute; left: 35px; width: 897px; top: 198px;
    font-size: 26.5px; line-height: 34px; text-align: justify;
  }

  .fee-table {
    position: absolute; left: 35px; top: 404px; width: 897px;
    border-collapse: separate; border-spacing: 0;
    border: 1px solid var(--rule); border-radius: 6px; overflow: hidden;
  }
  .fee-table th {
    height: 52px; font-size: 27px; font-weight: 700;
    border-bottom: 1px solid var(--rule); background: var(--paper);
  }
  .fee-table td {
    height: 50px; background: var(--band);
    font-size: 16.5px; font-weight: 700;
    border-bottom: 3px solid var(--paper);
  }
  .fee-table tr:last-child td { border-bottom: none; height: 48px; }
  .fee-table th + th, .fee-table td + td { border-left: 1px solid var(--rule); }
  .col-type { width: 395px; text-align: left; padding-left: 6px; padding-bottom: 4px; }
  .col-range { width: 251px; padding-left: 54px; text-align: left; }
  .col-retainer { width: 251px; text-align: center; }
  .fee-table th.col-type { text-align: center; padding: 0; }
  .fee-table th.col-range { text-align: center; padding: 0; }

  .contact-band {
    position: absolute; left: 35px; top: 1121px; width: 897px; height: 47px;
    background: var(--band); display: flex; align-items: center;
    justify-content: space-between; padding: 0 12px 0 6px; font-size: 11px;
  }
  .contact-item { display: flex; align-items: center; gap: 8px; }
  .contact-item svg { fill: none; stroke: var(--ink); stroke-width: 1.6; }
</style>
</head>
<body>
  <header class="brand">
    <div class="brand-mark"></div>
    <div class="brand-name"><small>THE LAW OFFICE OF</small>DANIEL M WHITFORD</div>
  </header>

  <h1 class="title">Average Fee Per Case Type</h1>
  <p class="intro">In order for our clients to set expectations for legal fees, we provide the national average range of fees per case type. These are only to provide you with an understanding of what other cases have cost clients in similar cases. Please note these are not estimates nor guarantees of your own legal costs.</p>

  <table class="fee-table">
    <thead>
      <tr><th class="col-type">Case Type</th><th class="col-range">Per Case Type</th><th class="col-retainer">Retainer</th></tr>
    </thead>
    <tbody>
      <tr><td class="col-type">Custody Contempt/Modification</td><td class="col-range">$5,000 - $8,000</td><td class="col-retainer">$3,500</td></tr>
      <tr><td class="col-type">Custody Initial</td><td class="col-range">$4,000 - $7,000</td><td class="col-retainer">$3,000</td></tr>
      <tr><td class="col-type">Custody &amp; Support</td><td class="col-range">$5,000 - $8,000</td><td class="col-retainer">$3,000</td></tr>
      <tr><td class="col-type">Support</td><td class="col-range">$2,000 - $4,000</td><td class="col-retainer">$3,000</td></tr>
      <tr><td class="col-type">Divorce (3301c)</td><td class="col-range">$1,500 - $3,000</td><td class="col-retainer">$2,000</td></tr>
      <tr><td class="col-type">Divorce (3301d)</td><td class="col-range">$2,000 - $3,000</td><td class="col-retainer">$2,500</td></tr>
      <tr><td class="col-type">Protection from Abuse</td><td class="col-range">$1,500 - $3,000</td><td class="col-retainer">$2,000</td></tr>
      <tr><td class="col-type">Divorce &amp; Custody</td><td class="col-range">$5,000 - $8,000</td><td class="col-retainer">$3,500</td></tr>
      <tr><td class="col-type">Divorce &amp; Equitable Distribution</td><td class="col-range">$6,000 - $10,000</td><td class="col-retainer">$3,500</td></tr>
      <tr><td class="col-type">Divorce, Custody &amp; Support</td><td class="col-range">$8,000 - $12,000</td><td class="col-retainer">$3,500</td></tr>
      <tr><td class="col-type">Divorce, Equitable Distribution &amp; Custody</td><td class="col-range">$10,000 - $15,000</td><td class="col-retainer">$5,000</td></tr>
      <tr><td class="col-type">Divorce, Equitable Distribution &amp; Support</td><td class="col-range">$8,000 - $12,000</td><td class="col-retainer">$3,500</td></tr>
      <tr><td class="col-type">Divorce, Equitable Distribution, Custody &amp; Support</td><td class="col-range">$12,000 - $15,000</td><td class="col-retainer">$3,500</td></tr>
    </tbody>
  </table>

  <footer class="contact-band">
    <div class="contact-item">
      <svg width="14" height="20" viewBox="0 0 14 20" aria-hidden="true"><path d="M7 19C7 19 1 11 1 7a6 6 0 0 1 12 0c0 4-6 12-6 12z" fill="#3b3b91" stroke="none"/><circle cx="7" cy="7" r="2.3" fill="#9bdcf6" stroke="none"/></svg>
      <span>This is your address</span>
    </div>
    <div class="contact-item">
      <svg width="14" height="16" viewBox="0 0 14 16" aria-hidden="true"><path d="M3 1l3 3-2 2c1 2 3 5 5 6l2-2 3 3-2 2C6 15 1 8 1 3z" fill="#3b3b91" stroke="none"/></svg>
      <span>00-343-12345</span>
    </div>
    <div class="contact-item">
      <svg width="20" height="20" viewBox="0 0 20 20" aria-hidden="true"><circle cx="10" cy="10" r="8.5"/><ellipse cx="10" cy="10" rx="4" ry="8.5"/><path d="M1.5 10h17M3 5.5h14M3 14.5h14"/></svg>
      <span>www.whitfordlaw.com</span>
    </div>
  </footer>
</body>
</html>
```